Tree company needs modern website design

We need a website design for a tree company, here are some websites they like:

http://korvalemarine.com/company/ - we like the big image filling most of the page. Also the top half of the page looks good with the logo along top and good task bar also (we don’t like the spiel on left hand side covering up the picture + too many words!) If we could have our logo at lop like this along with our slogan which is 'Great Looking Trees that Grow Well'

http://www.pinecroftgardens.co.nz/ - we like the bottom half of this with the clean lines and welcome to part down bottom rather than the spiel to the left as on above site. Also like the moving leaves, any chance we could have birds such as a fantail, Tui and Bellbirds flying across the page and also some birdsong playing?

This is their existing website, that needs an updated design: http://tallfernwood.co.nz/

Industry/Entity Type

It Company

Font styles to use
Serif
Sans Serif

Requirements
Must have
• "Website by Pages Built Simple" located in bottom right hand side
Use images provided as background or banner images
Should not have
• Social Media icons

```html
<!DOCTYPE html>
<html lang="en">
<head>
<meta charset="utf-8">
<title>Tall Fernwood Trees</title>
<link href="https://fonts.googleapis.com/css2?family=Ubuntu:wght@300;400;500&family=Open+Sans:ital,wght@0,400;0,600;1,400&display=swap" rel="stylesheet">
<style>
:root{
  --green:#8cc63f;
  --green-light:#b5e07a;
  --green-pale:#c9ec95;
  --ink:#333;
  --text:#666;
  --line:#e6e6e6;
  --quote-bg:#f4f0f0;
  --footer:#3a3a3c;
  --footer-deep:#2b2b2d;
  --footer-strip:#e4e4e6;
  --white:#fff;
}
*{box-sizing:border-box;margin:0;padding:0}
html,body{width:907px;height:1200px;overflow:hidden;background:var(--white)}
body{position:relative;font-family:"Open Sans",Arial,sans-serif;color:var(--text);font-size:9px}
.abs{position:absolute}
h2,h3,.nav a,.hero-title,.brand,.f-brand,.f-head{font-family:"Ubuntu",Arial,sans-serif}

/* header */
.site-header{left:0;top:0;width:907px;height:56px;background:var(--white);border-bottom:1px solid var(--line)}
.brand{left:148px;top:13px;display:flex;align-items:center;gap:6px;font-size:13px;font-weight:500;color:var(--green);letter-spacing:.3px}
.brand-mark{width:13px;height:13px;background:var(--green)}
.slogan{left:167px;top:33px;font-size:7px;color:#888;letter-spacing:.2px}
.nav{right:150px;top:0;display:flex;gap:26px;height:56px}
.nav a{font-size:9.5px;color:#555;text-decoration:none;padding-top:22px;border-top:3px solid transparent}
.nav a.active{color:var(--green);border-top-color:var(--green)}

/* hero */
.hero{left:0;top:56px;width:907px;height:280px;background:linear-gradient(180deg,#b9cde0 0%,#9fb7c9 22%,#4f6a3a 45%,#324a27 70%,#5c5f4e 100%)}
.hero-title{left:150px;top:147px;width:285px;background:var(--white);padding:4px 8px;font-size:23px;font-weight:300;line-height:28px;color:#222}
.hero-btn{left:150px;top:249px;width:131px;height:30px;background:var(--green-light);border:1px solid #9ccc5c;display:flex;align-items:center;gap:14px;padding-left:8px;font-size:8px;color:#6a8f3a;letter-spacing:.5px}
.hero-arrow{top:165px;width:26px;height:38px;background:rgba(0,0,0,.35);display:flex;align-items:center;justify-content:center}

/* intro columns */
.intro{top:383px;width:196px}
.intro h3{font-size:11.5px;font-weight:400;color:var(--ink);margin-bottom:14px}
.intro p{font-size:7.5px;line-height:13px;color:#555}
.more{display:block;text-align:right;margin-top:14px;font-size:7.5px;color:#444}
.more.on{color:var(--green)}

/* projects */
.section-title{font-size:11px;font-weight:500;color:var(--ink)}
.rule{height:1px;background:var(--line)}
.car-arrow{top:602px;width:19px;height:19px;background:#c8c8c8;display:flex;align-items:center;justify-content:center}
.thumb{top:568px;width:117px;height:77px}
.thumb-active{background:var(--green-pale);border:1px solid #a9d36c;text-align:center;font-size:7px;color:#333;line-height:9px;padding-top:16px}
.thumb-active b{font-weight:600;display:block;margin-top:6px}
.ic{display:inline-block;width:15px;height:15px;border-radius:50%;background:#333;margin:0 3px}

/* why & quote */
.why li{list-style:none;display:flex;align-items:center;gap:9px;font-size:7.5px;color:#555;height:22.3px}
.tick{width:11px;height:11px;border-radius:50%;background:var(--green);display:flex;align-items:center;justify-content:center}
.quote{left:463px;top:757px;width:293px;height:98px;background:var(--quote-bg);padding:14px 16px;font-style:italic;font-size:7px;line-height:12px;color:#777}
.author{left:463px;top:866px;display:flex;align-items:center;gap:8px;font-size:7.5px;color:#444}
.avatar{width:15px;height:15px;background:#555}

/* footer */
.footer-strip{left:0;top:963px;width:907px;height:12px;background:var(--footer-strip)}
.footer{left:0;top:975px;width:907px;height:187px;background:var(--footer)}
.f-head{font-size:8px;font-weight:500;color:#eee;letter-spacing:.3px}
.f-brand{left:148px;top:1000px;display:flex;align-items:center;gap:5px;font-size:10px;font-weight:500;color:var(--green)}
.f-brand span{width:10px;height:10px;background:var(--green)}
.f-about{left:148px;top:1030px;width:130px;font-style:italic;font-size:7px;line-height:11px;color:#7c7c80}
.posts li{list-style:none;font-size:7.5px;color:#ddd;border-bottom:1px solid #4a4a4d;padding:8px 0 9px;width:140px}
.grid{display:grid;grid-template-columns:repeat(4,33px);gap:3px}
.grid i{display:block;height:33px;background:#e5e5e7}
.contact p{font-size:7.5px;line-height:12px;color:#eee}
.bottom-bar{left:0;top:1162px;width:907px;height:38px;background:var(--footer-deep)}
.copyright{left:148px;top:1177px;font-size:6.5px;color:#aaa}
.credit{right:150px;top:1177px;font-size:6.5px;color:#aaa}
</style>
</head>
<body>

<header class="site-header abs">
  <div class="brand abs"><span class="brand-mark"></span>TALL FERNWOOD TREES</div>
  <p class="slogan abs">Great Looking Trees that Grow Well</p>
  <nav class="nav abs">
    <a class="active">Home</a><a>About Us</a><a>Tree Gallery</a><a>Projects</a><a>Catalogue</a><a>Contact Us</a>
  </nav>
</header>

<section class="hero abs" role="img" aria-label="Photo of tall mature trees lining a driveway under a blue sky"></section>
<h1 class="hero-title abs">Do you need semi mature trees for instant effect?</h1>
<div class="hero-btn abs">
  <svg width="13" height="13" viewBox="0 0 13 13"><circle cx="6.5" cy="6.5" r="6.5" fill="#6fae2c"/><path d="M3.5 6.7l2 2 4-4" stroke="#fff" stroke-width="1.6" fill="none"/></svg>
  CONTACT US
</div>
<div class="hero-arrow abs" style="left:0"><svg width="8" height="12"><path d="M6 1L1 6l5 5" stroke="#fff" stroke-width="2" fill="none"/></svg></div>
<div class="hero-arrow abs" style="right:0"><svg width="8" height="12"><path d="M2 1l5 5-5 5" stroke="#fff" stroke-width="2" fill="none"/></svg></div>

<article class="intro abs" style="left:148px">
  <h3>About Us</h3>
  <p>Lid est laborum dolo rumes fugats untras. Etharums ser quidem rerum facilis dolores nemis omnis fugats vitaes nemo minima rerums unsers sadips amets.</p>
  <span class="more">Learn More ›</span>
</article>
<article class="intro abs" style="left:357px">
  <h3>Tree Gallery</h3>
  <p>Lid est laborum dolo rumes fugats untras. Etharums ser quidem rerum facilis dolores nemis omnis fugats vitaes nemo minima rerums unsers sadips amets.</p>
  <span class="more">Learn More ›</span>
</article>
<article class="intro abs" style="left:563px">
  <h3>Catalogue</h3>
  <p>Lid est laborum dolo rumes fugats untras. Etharums ser quidem rerum facilis dolores nemis omnis fugats vitaes nemo minima rerums unsers sadips amets.</p>
  <span class="more on">Learn More ›</span>
</article>

<h2 class="section-title abs" style="left:151px;top:535px">Projects</h2>
<div class="rule abs" style="left:235px;top:542px;width:524px"></div>
<div class="car-arrow abs" style="left:148px"><svg width="6" height="9"><path d="M5 1L1 4.5 5 8" stroke="#fff" stroke-width="1.5" fill="none"/></svg></div>
<div class="car-arrow abs" style="left:740px"><svg width="6" height="9"><path d="M1 1l4 3.5L1 8" stroke="#fff" stroke-width="1.5" fill="none"/></svg></div>
<div class="thumb abs" style="left:188px;background:linear-gradient(180deg,#7fa8d6,#c9d3d8 55%,#8a8f82)" role="img" aria-label="Photo of a modern building with new trees"></div>
<div class="thumb thumb-active abs" style="left:324px">
  <span class="ic"></span><span class="ic"></span>
  <b>Project Title</b>Tree Project
</div>
<div class="thumb abs" style="left:463px;background:linear-gradient(180deg,#6f9fd8,#c8ccd0 45%,#6c7a4a)" role="img" aria-label="Photo of mountains behind a planted property"></div>
<div class="thumb abs" style="left:603px;background:linear-gradient(180deg,#4f8ad6,#b9cbe0 40%,#4d6e38)" role="img" aria-label="Photo of a tree lined road"></div>

<h2 class="section-title abs" style="left:151px;top:722px;font-weight:400">Why Choose Us?</h2>
<div class="rule abs" style="left:250px;top:729px;width:198px"></div>
<ul class="why abs" style="left:151px;top:752px">
  <li><span class="tick"><svg width="6" height="6"><path d="M1 3h4M3 1l2 2-2 2" stroke="#fff" fill="none"/></svg></span>Cras rutrum leo at odio volutpat id blandit fugiats ipsum ornare.</li>
  <li><span class="tick"><svg width="6" height="6"><path d="M1 3h4M3 1l2 2-2 2" stroke="#fff" fill="none"/></svg></span>Donec fermentum porttitor nunc, sit amet gravida est porttitor vel.</li>
  <li><span class="tick"><svg width="6" height="6"><path d="M1 3h4M3 1l2 2-2 2" stroke="#fff" fill="none"/></svg></span>Maecenas quis nisi in urctus adipiscing sed vehicula tellus amet dolore.</li>
  <li><span class="tick"><svg width="6" height="6"><path d="M1 3h4M3 1l2 2-2 2" stroke="#fff" fill="none"/></svg></span>Aenean faucibus sapien a odio varius aliquet volutpats sadips.</li>
  <li><span class="tick"><svg width="6" height="6"><path d="M1 3h4M3 1l2 2-2 2" stroke="#fff" fill="none"/></svg></span>Suspendisse venenatis euismod ve vestibulum volutpat nibh imperdiets.</li>
  <li><span class="tick"><svg width="6" height="6"><path d="M1 3h4M3 1l2 2-2 2" stroke="#fff" fill="none"/></svg></span>Quisque non leo molestie augue imperdiet sollicitudin eu nec urna.</li>
</ul>

<h2 class="section-title abs" style="left:460px;top:722px;font-weight:400">What Client's Say</h2>
<div class="rule abs" style="left:568px;top:729px;width:190px"></div>
<blockquote class="quote abs">"Neque porro quisquam est, qui dolorem ipsum quia dolor sit amet, consec tetur, adipisci velit, sed quia non numquam eius modi tempora incidunt utis labore et dolore magnam aliquam quaerat voluptatem. Ut enim ad minimas veniam, quis nostrum exercitationem ullam corporis suscipit laboriosam, nisi ut aliquid ex ea commodi consequatur slores amet untras vel illum qui."</blockquote>
<svg class="abs" style="left:486px;top:855px" width="12" height="8"><path d="M0 0h12L0 8z" fill="#f4f0f0"/></svg>
<div class="author abs"><span class="avatar"></span><span><b style="font-weight:600">Jon Doe,</b> Company Inc.</span></div>

<div class="footer-strip abs"></div>
<footer class="footer abs"></footer>
<div class="f-brand abs"><span></span>TALL FERNWOOD TREES</div>
<p class="f-about abs">Lorem ipsum ex vix illud nonummy, novum tation et his. At vix scriptaset patrioque scribentur, at pro fugit erts verterem molestiae, sed et vivendo ali Lorem ipsum ex vix illud nonummy, novum tation et his. At vix scripta patrioque scribentur...</p>

<h3 class="f-head abs" style="left:304px;top:1004px">RECENT POSTS</h3>
<ul class="posts abs" style="left:304px;top:1021px">
  <li>Voluptas Sadips Ipsums Dolors Untra</li>
  <li>Fugiats Litora Ultricies Ante Auctor</li>
  <li>Sapien Litora Dolores Ultrices</li>
  <li>Nemis Fugiats Voluptas Dolores Uns</li>
</ul>

<h3 class="f-head abs" style="left:460px;top:1004px">RECENT PROJECTS</h3>
<div class="grid abs" style="left:460px;top:1033px"><i></i><i></i><i></i><i></i><i></i><i></i><i></i><i></i></div>

<h3 class="f-head abs" style="left:667px;top:1004px;font-weight:400">CONTACT INFORMATION</h3>
<div class="contact abs" style="left:667px;top:1030px">
  <p>58 Kowhai Lane, Ashvale 9420</p>
  <p>Toll free: 0508 440 771</p>
  <p>Ph: (03) 440 7712</p>
  <p>Fax: (03) 440 7719</p>
  <p>Email: sales@tallfernwood.co.nz</p>
</div>

<div class="bottom-bar abs"></div>
<p class="copyright abs">Copyright 2014 Tall Fernwood Trees | All Rights Reserved</p>
<p class="credit abs">Website by Pages Built Simple</p>

</body>
</html>
```